Brill's Jewelers website (www.brillsjewelers-example.com)

We are in need of a web storefront for a retail Jewelry store.
www.brillsjewelers-example.com
https://www.facebook.com/Brills-Jewelers-Palm-Harbor-731450928814265/

Brill's Jewelers is located in Coral Gables, Florida. The store has been family owned and operated since 1958. Their focus customers are high-income families that care about quality over the brand name. They mostly sell fashion jewelry and diamonds up to 8 carats. We are looking for a simple minimalistic site that their customers can view their inventory and purchase items online.

Competitors websites:
https://www.tovinjewelers-example.com/
http://www.varelso-example.com/
http://craftedringshop-example.com/

Pages:
-Home (with message bulletin)
-Jewelry
We would be able to create the subpages ie Rings, Bracelets, Earrings, Necklaces, Estate, Watches, Men's, Children's
-Services
We would need sub pages ie Appraisals, Consignment, Repairs
-About us
-Contact

Target Market(s)

Local wealthy families

Coding

Coded - Design and coding required

Number of Pages Required

5+ page

Font styles to use
Serif

Requirements
Must have
• -An E-commerce site customers can buy jewelry online.
-An easy process internally to add new items to the site
-Colors are Black and White or Black and Gold
Nice to have
• I would like to stay away from face shots of random models in stock photos. I want the jewelry pieces as the focus, not models.

```html
<!DOCTYPE html>
<html lang="en">
<head>
<meta charset="utf-8">
<title>Brill's Jewelers</title>
<link href="https://fonts.googleapis.com/css2?family=Montserrat:wght@400;600;700;800&family=Open+Sans:wght@400;600;700&display=swap" rel="stylesheet">
<style>
:root{
  --black:#0b0b0b;
  --ink:#1b1b1b;
  --gold:#d6a83e;
  --white:#ffffff;
  --grey:#b5b5b5;
  --grey-light:#e6e6e6;
  --text:#555555;
}
*{box-sizing:border-box;margin:0;padding:0}
html,body{width:1200px;height:3604px;overflow:hidden}
body{font-family:"Open Sans",Arial,sans-serif;color:var(--ink);background:var(--white);position:relative}
h1,h2,h3,.brand,.btn,.nav a{font-family:"Montserrat",Arial,sans-serif}
.btn{display:inline-block;font-size:13px;font-weight:700;letter-spacing:.5px;text-transform:uppercase;padding:12px 28px;color:var(--white);text-align:center}
.btn-gold{background:var(--gold)}
.btn-grey{background:var(--grey)}

/* header + hero */
.hero{position:absolute;top:0;left:0;width:1200px;height:610px;background:radial-gradient(ellipse at 70% 60%,#2a2a2a 0%,#0b0b0b 60%)}
.topbar{position:absolute;top:44px;left:108px;right:108px;display:flex;align-items:center}
.brand{color:var(--white);font-size:22px;font-weight:600;display:flex;align-items:center;gap:10px;white-space:nowrap}
.brand i{width:12px;height:12px;border-radius:50%;background:var(--white);display:block}
.nav{display:flex;gap:30px;margin-left:90px}
.nav a{color:var(--white);text-decoration:none;font-size:14px;font-weight:600}
.nav a.active{color:var(--gold)}
.cart{margin-left:auto;color:var(--white);font-family:"Montserrat",sans-serif;font-size:14px;font-weight:600;display:flex;align-items:center;gap:8px}
.cart b{color:var(--gold)}
.hero-copy{position:absolute;left:108px;top:236px;width:500px;color:var(--white)}
.hero-copy h1{font-size:34px;font-weight:800;line-height:1.15;margin-bottom:14px;white-space:nowrap}
.hero-copy p{font-size:17px;font-weight:600;line-height:1.45;margin-bottom:36px}
.hero-photo{position:absolute;left:640px;top:150px;width:440px;height:420px;border-radius:8px;background:radial-gradient(circle at 50% 45%,#cfcfd6 0%,#7c7c86 35%,#1c1c1f 75%)}
.slide-arrow{position:absolute;color:var(--white);font-size:28px;font-weight:700;font-family:"Montserrat",sans-serif}

.section-title{text-align:center;font-size:36px;font-weight:700;text-transform:uppercase}

/* featured */
.featured{position:absolute;top:610px;left:0;width:1200px;height:710px;background:var(--white)}
.featured .section-title{position:absolute;top:76px;width:100%}
.tabs{position:absolute;top:132px;width:100%;display:flex;justify-content:center;gap:26px;font-family:"Montserrat",sans-serif;font-size:13px;font-weight:700}
.tabs span.active{color:var(--gold);border-bottom:2px solid var(--gold);padding-bottom:4px}
.cards{position:absolute;left:108px;width:984px;display:flex;justify-content:space-between}
.card{position:relative;width:316px;height:368px;background:var(--white);border:1px solid var(--grey-light);box-shadow:0 2px 10px rgba(0,0,0,.08);text-align:center;padding-top:22px}
.card .thumb{width:200px;height:150px;margin:0 auto 16px;border-radius:4px}
.card h3{font-size:21px;font-weight:700;line-height:1.2;margin-bottom:10px}
.card .price{font-family:"Montserrat",sans-serif;font-weight:700;font-size:19px;margin-bottom:16px}
.card .price b{color:var(--gold)}
.card .btn{width:250px}
.tag{position:absolute;top:10px;right:14px;background:var(--gold);color:var(--white);font-size:11px;font-weight:700;padding:3px 14px}
.featured .cards{top:190px}
.view-more{position:absolute;top:596px;left:468px;width:264px}

/* new arrivals */
.arrivals{position:absolute;top:1320px;left:0;width:1200px;height:600px;background:radial-gradient(ellipse at 75% 30%,#2a2a2a 0%,#050505 65%)}
.arrivals .section-title{position:absolute;top:70px;width:100%;color:var(--white)}
.arrivals .cards{top:148px}
.arrivals .card{height:372px}
.side-arrow{position:absolute;top:308px;width:42px;height:42px;background:#2c2c2c;color:var(--white);display:flex;align-items:center;justify-content:center;font-size:22px;font-weight:700}

/* testimonial */
.testimonial{position:absolute;top:1920px;left:0;width:1200px;height:600px;background:var(--white)}
.photo{position:absolute;border-radius:2px}
.testi-copy{position:absolute;left:628px;top:136px;width:450px}
.testi-copy h2{font-size:34px;font-weight:700;margin-bottom:26px}
.quote{color:var(--gold);font-size:70px;font-family:Georgia,serif;line-height:.6;font-weight:700;margin-bottom:18px}
.testi-copy p{color:#a5a5a5;font-size:15px;line-height:1.75;margin-bottom:18px}
.author{font-size:14px;color:var(--text);display:flex;align-items:center;gap:10px}
.author::before{content:"";width:40px;height:2px;background:var(--gold)}
.author b{color:var(--gold)}
.pager{display:flex;gap:12px;margin-top:40px}
.pager span{width:40px;height:40px;border-radius:50%;display:flex;align-items:center;justify-content:center;font-weight:700;color:var(--white)}

/* models */
.models{position:absolute;top:2520px;left:0;width:1200px;height:700px;background:var(--black)}
.models .section-title{position:absolute;top:76px;width:100%;color:var(--white)}
.models-grid{position:absolute;top:152px;left:108px;width:984px;height:470px;display:grid;grid-template-columns:262px 220px 248px 226px;grid-template-rows:228px 228px;gap:14px 9px}
.tile{border-radius:2px}
.tile-wide{grid-column:1/3;position:relative}
.tile-wide .btn{position:absolute;left:120px;top:106px;padding:10px 40px}
.tile-bottom{grid-column:3/5}

/* footer */
.footer{position:absolute;top:3220px;left:0;width:1200px;height:384px;background:var(--white)}
.foot-cols{position:absolute;top:78px;left:108px;width:984px;display:flex;justify-content:space-between}
.foot-col{width:220px}
.foot-col h3{font-size:19px;font-weight:700;text-transform:uppercase;margin-bottom:18px}
.foot-col li{list-style:none;font-size:14px;color:var(--text);line-height:1.8}
.foot-col p{font-size:14px;color:var(--text);line-height:1.6;margin-bottom:22px}
.subscribe{display:flex;width:250px;height:46px}
.subscribe span{flex:1;border:1px solid var(--grey-light);font-size:13px;color:#999;padding:14px 10px}
.subscribe b{background:var(--gold);color:var(--white);font-size:13px;font-family:"Montserrat",sans-serif;padding:15px 14px}
.foot-bar{position:absolute;top:300px;left:108px;width:984px;border-top:1px solid var(--grey-light);padding-top:26px;display:flex;align-items:center}
.socials{display:flex;gap:10px}
.socials i{width:34px;height:34px;border-radius:50%;display:block}
.copy{margin-left:auto;font-size:13px;color:var(--text)}
</style>
</head>
<body>

<section class="hero">
  <div class="topbar">
    <div class="brand"><i></i>Brill's Jewelers</div>
    <nav class="nav">
      <a class="active">HOME</a><a>JEWELRY</a><a>SERVICES</a><a>ABOUT US</a><a>CONTACT</a>
    </nav>
    <div class="cart">
      <svg width="16" height="16" viewBox="0 0 16 16"><path d="M1 2h2l2 8h8l2-6H4" fill="none" stroke="#fff" stroke-width="1.6"/><circle cx="6" cy="13.5" r="1.3" fill="#fff"/><circle cx="12" cy="13.5" r="1.3" fill="#fff"/></svg>
      CART <b>$0.00</b>
    </div>
  </div>
  <div class="hero-copy">
    <h1>SELL JEWELLERY ONLINE</h1>
    <p>Lorem ipsum dolor sit amet, consectetur adipiscing elit, sed do eiusmod tempor incididunt ut labore</p>
    <span class="btn btn-gold">GET STARTED</span>
  </div>
  <div class="hero-photo" role="img" aria-label="Photo of diamond engagement rings and a pear-cut diamond ring"></div>
  <span class="slide-arrow" style="left:42px;top:280px">‹</span>
  <span class="slide-arrow" style="right:42px;top:280px">›</span>
</section>

<section class="featured">
  <h2 class="section-title">Featured Product</h2>
  <div class="tabs">
    <span class="active">ALL</span><span>RINGS</span><span>BRACELETS</span><span>EARRINGS</span><span>NECKLACES</span><span>ESTATE</span><span>WATCHES</span><span>MEN'S</span><span>CHILDREN'S</span>
  </div>
  <div class="cards">
    <div class="card">
      <div class="thumb" role="img" aria-label="Photo of a diamond ring" style="background:radial-gradient(circle,#f2f2f2 0%,#cfcfcf 70%,#fff 100%)"></div>
      <h3>Lorem ipsum dolor<br>sit amet</h3>
      <div class="price">Price : <b>$50.00</b></div>
      <span class="btn btn-grey">ADD TO CART</span>
    </div>
    <div class="card">
      <span class="tag">New</span>
      <div class="thumb" role="img" aria-label="Photo of a wristwatch with blue dial" style="background:radial-gradient(circle,#3b4f7a 0%,#9a9ea8 45%,#fff 75%)"></div>
      <h3>Lorem ipsum dolor<br>sit amet</h3>
      <div class="price">Price : <b>$50.00</b></div>
      <span class="btn btn-gold">ADD TO CART</span>
    </div>
    <div class="card">
      <div class="thumb" role="img" aria-label="Photo of two gold wedding bands" style="background:radial-gradient(circle,#e6c07a 0%,#c9a160 40%,#fff 75%)"></div>
      <h3>Lorem ipsum dolor<br>sit amet</h3>
      <div class="price">Price : <b>$50.00</b></div>
      <span class="btn btn-grey">ADD TO CART</span>
    </div>
  </div>
  <span class="btn btn-gold view-more">VIEW MORE PRODUCT</span>
</section>

<section class="arrivals">
  <h2 class="section-title">New Arrivals</h2>
  <div class="side-arrow" style="left:28px">‹</div>
  <div class="side-arrow" style="right:28px">›</div>
  <div class="cards">
    <div class="card">
      <div class="thumb" role="img" aria-label="Photo of diamond drop earrings" style="background:radial-gradient(circle,#dcdcdc 0%,#f4f4f4 55%,#fff 80%)"></div>
      <h3>Lorem ipsum dolor<br>sit amet</h3>
      <div class="price">Price : <b>$50.00</b></div>
      <span class="btn btn-grey">LEARN MORE</span>
    </div>
    <div class="card">
      <span class="tag">New</span>
      <div class="thumb" role="img" aria-label="Photo of a silver chain necklace" style="background:radial-gradient(circle,#c4c4c4 0%,#ececec 55%,#fff 80%)"></div>
      <h3>Lorem ipsum dolor<br>sit amet</h3>
      <div class="price">Price : <b>$50.00</b></div>
      <span class="btn btn-gold">LEARN MORE</span>
    </div>
    <div class="card">
      <div class="thumb" role="img" aria-label="Photo of a gold watch with leather strap" style="background:radial-gradient(circle,#c9a04a 0%,#3a2a1a 45%,#fff 78%)"></div>
      <h3>Lorem ipsum dolor<br>sit amet</h3>
      <div class="price">Price : <b>$50.00</b></div>
      <span class="btn btn-grey">LEARN MORE</span>
    </div>
  </div>
</section>

<section class="testimonial">
  <div class="photo" role="img" aria-label="Photo of a couple at an evening event" style="left:108px;top:136px;width:376px;height:296px;background:linear-gradient(160deg,#6d7a6a,#2d2a2a 60%,#8a7a70)"></div>
  <div class="photo" role="img" aria-label="Photo of a wristwatch" style="left:388px;top:52px;width:200px;height:200px;border:6px solid #fff;background:radial-gradient(circle,#7a5a40,#2b2420 70%)"></div>
  <div class="photo" role="img" aria-label="Photo of yellow gemstone earrings" style="left:402px;top:404px;width:162px;height:172px;border:6px solid #fff;background:radial-gradient(circle,#e8c74a,#8a9aa0 70%)"></div>
  <div class="testi-copy">
    <h2>CLIENT TESTIMONIAL</h2>
    <div class="quote">“</div>
    <p>Lorem ipsum dolor sit amet, consectetur adipiscing elit, sed do eiusmod tempor incididunt ut labore et dolore magna aliqua. Ut enim ad minim veniam, quis nostrud exercitation ullamco laboris nisi ut aliquip ex ea commodo consequat.</p>
    <div class="author"><span><b>DANA MORROW</b> Manager, Company name</span></div>
    <div class="pager"><span style="background:#c8c8c8">‹</span><span style="background:var(--gold)">›</span></div>
  </div>
</section>

<section class="models">
  <h2 class="section-title">Our Jewelers Models</h2>
  <div class="models-grid">
    <div class="tile tile-wide" role="img" aria-label="Photo of a gold bar pendant necklace" style="background:linear-gradient(135deg,#3a3f4a,#1e2228)"><span class="btn btn-gold">LEARN MORE</span></div>
    <div class="tile" role="img" aria-label="Photo of a gold ring with diamond" style="background:radial-gradient(circle,#c99a55,#2a1d12 75%)"></div>
    <div class="tile" role="img" aria-label="Photo of a sapphire ring surrounded by diamonds" style="background:radial-gradient(circle,#2d4fa8,#0c1226 70%)"></div>
    <div class="tile" role="img" aria-label="Photo of gold leaf earrings" style="background:linear-gradient(135deg,#22201c,#3a342a)"></div>
    <div class="tile" role="img" aria-label="Photo of diamond drop earrings" style="background:linear-gradient(135deg,#2a2a2a,#4a4a4a)"></div>
    <div class="tile tile-bottom" role="img" aria-label="Photo of loose diamonds and stud earrings" style="background:linear-gradient(135deg,#1a1f2a,#4a5260 60%,#20242c)"></div>
  </div>
</section>

<footer class="footer">
  <div class="foot-cols">
    <div class="foot-col">
      <h3>Information</h3>
      <ul><li>About Us</li><li>Latest From Social Feed</li><li>Latest Videos</li><li>Our Services</li><li>Meet Our Jeweler</li><li>Create A Wish List</li></ul>
    </div>
    <div class="foot-col">
      <h3>Designers</h3>
      <ul><li>Halden Studio</li><li>Orrin &amp; Vale</li><li>Luma Collection</li><li>Marisette Atelier</li><li>Everline Bands</li><li>Solenne Bands</li></ul>
    </div>
    <div class="foot-col">
      <h3>Contact Brill's</h3>
      <ul><li>Send Us A Message</li><li>Get Directions</li><li>Make An Appointment</li></ul>
    </div>
    <div class="foot-col" style="width:250px">
      <h3>Subscribe</h3>
      <p>Be a part of our family by subscribing to the newsletter.</p>
      <div class="subscribe"><span>Email Address</span><b>SUBSCRIBE</b></div>
    </div>
  </div>
  <div class="foot-bar">
    <div class="socials"><i style="background:#9a9a9a"></i><i style="background:var(--gold)"></i><i style="background:#9a9a9a"></i></div>
    <div class="copy">© 2020 Brill's Jewelers All Rights Reserved</div>
  </div>
</footer>

</body>
</html>
```